VORK Business Cards, Letterhead and Envelopes
Business Cards, Letterhead and Envelopes
Simple
Rajendran P Subbiah
Dirección TI - ERP Quandrel
Calle Tepozan 58,
Col. Las Brisas,
Distrito Federal
Mexico - 04260
rajen@vorkitel.mx
www.vorkitel.mx, www.vorkitel.in

```html
<!DOCTYPE html>
<html lang="es">
<head>
<meta charset="utf-8">
<title>VORK Stationery</title>
<link rel="stylesheet" href="https://fonts.googleapis.com/css2?family=Tinos:wght@400;700&display=swap">
<style>
:root{
  --blue:#1f5fbf;
  --blue-dark:#164a99;
  --grey:#8a8a8a;
  --grey-dark:#6f6f6f;
  --paper:#ffffff;
  --ink:#2a2a2a;
  --line:#c9c9c9;
  --faint:#e6ecf5;
}
*{margin:0;padding:0;box-sizing:border-box}
html,body{width:1200px;height:749px;overflow:hidden;background:var(--paper)}
body{position:relative;font-family:"Tinos",serif;color:var(--ink)}
.sheet{position:absolute;overflow:hidden;background:var(--paper)}
.sheet svg.bg{position:absolute;inset:0;width:100%;height:100%}
.brand{position:absolute;display:flex;align-items:center;gap:.3em;font-family:"Tinos",serif;font-weight:700;color:var(--blue);letter-spacing:.02em;line-height:1}
.brand .mark{width:.8em;height:.8em;background:currentColor}
.brand.on-dark{color:var(--paper)}
.faint-name{position:absolute;font-family:"Tinos",serif;font-weight:700;color:var(--faint);line-height:1}

.letterhead{left:58px;top:72px;width:452px;height:648px;border:1px solid var(--line)}
.letterhead .brand{left:34px;top:30px;font-size:54px}
.letterhead .faint-name{left:30px;top:460px;font-size:120px}
.letterhead .contact{position:absolute;left:40px;bottom:22px;font-size:10px;line-height:1.45}
.letterhead .contact a{color:var(--blue);text-decoration:none}

.card{border:1px solid var(--line)}
.card-front{left:576px;top:48px;width:216px;height:132px}
.card-front .brand{left:40px;top:10px;font-size:24px}
.card-front .person{position:absolute;left:40px;top:44px;font-size:8px;text-align:center;width:140px;line-height:1.3}
.card-front .person .name{color:var(--blue);font-size:9px}
.card-front .address{position:absolute;left:16px;top:78px;font-size:6px;line-height:1.35}
.card-front .address span{color:var(--blue)}

.card-back-white{left:816px;top:53px;width:221px;height:115px}
.card-back-white .brand{left:52px;top:38px;font-size:30px}

.card-blue{left:576px;top:204px;width:216px;height:132px;background:var(--blue);border:none}
.card-blue .brand{left:40px;top:44px;font-size:32px}

.card-grey-back{left:912px;top:228px;width:216px;height:132px;background:var(--grey-dark);border:none}
.card-grey-front{left:758px;top:252px;width:226px;height:132px;background:var(--grey);border:none;box-shadow:2px 2px 6px rgba(0,0,0,.25)}
.card-grey-front .brand{left:52px;top:48px;font-size:32px}
.card-grey-back .mark-only{position:absolute;left:96px;top:52px;width:24px;height:24px;background:var(--paper)}

.envelope{left:576px;top:396px;width:552px;height:324px;border:1px solid var(--line)}
.envelope .flap-mark{position:absolute;left:266px;top:28px;width:22px;height:22px;background:var(--paper)}
.envelope .brand{left:20px;top:168px;font-size:52px}
.envelope .sender{position:absolute;left:24px;top:238px;font-size:9px;line-height:1.4}
.envelope .faint-name{left:250px;top:220px;font-size:80px}
</style>
</head>
<body>

<section class="sheet letterhead" aria-label="Letterhead">
  <svg class="bg" viewBox="0 0 452 648" preserveAspectRatio="none" aria-hidden="true">
    <path d="M0 0H452V170C380 70 230 20 0 14Z" fill="var(--blue)"/>
    <path d="M0 14C230 20 380 70 452 170" fill="none" stroke="var(--line)" stroke-width="2"/>
  </svg>
  <div class="brand"><span class="mark"></span>VORK</div>
  <div class="faint-name" aria-hidden="true">VORK</div>
  <div class="contact">
    Calle Tepozan 58, Col. Las Brisas, Distrito Federal, Mexico - 04260<br>
    Phone: +52 (55) 5010 2284 / +52 (55) 5010 2291<br>
    Email: <a>rajen@vorkitel.mx</a> | <a>www.vorkitel.mx</a>, <a>www.vorkitel.in</a>
  </div>
</section>

<section class="sheet card card-front" aria-label="Business card front">
  <svg class="bg" viewBox="0 0 216 132" preserveAspectRatio="none" aria-hidden="true">
    <path d="M120 0H216V60C200 25 165 6 120 0Z" fill="var(--blue)"/>
  </svg>
  <div class="brand"><span class="mark"></span>VORK</div>
  <div class="person"><div class="name">Rajendran P Subbiah</div>Dirección TI - ERP Quandrel</div>
  <div class="address">Calle Tepozan 58, Col. Las Brisas, Distrito Federal, Mexico - 04260<br>
    Tel: +52 (55) 5010 2284 / +52 (55) 5010 2291<br>
    <span>rajen@vorkitel.mx</span> | <span>www.vorkitel.mx, www.vorkitel.in</span></div>
</section>

<section class="sheet card card-back-white" aria-label="Business card back">
  <div class="brand"><span class="mark"></span>VORK</div>
</section>

<section class="sheet card card-blue" aria-label="Business card blue">
  <div class="brand on-dark"><span class="mark"></span>VORK</div>
</section>

<section class="sheet card card-grey-back" aria-label="Business card grey back">
  <svg class="bg" viewBox="0 0 216 132" preserveAspectRatio="none" aria-hidden="true">
    <path d="M60 20C120 20 170 40 200 90" fill="none" stroke="#9a9a9a" stroke-width="2"/>
  </svg>
  <div class="mark-only"></div>
</section>

<section class="sheet card card-grey-front" aria-label="Business card grey front">
  <svg class="bg" viewBox="0 0 226 132" preserveAspectRatio="none" aria-hidden="true">
    <path d="M100 0H226V70C205 30 160 6 100 0Z" fill="#9c9c9c"/>
  </svg>
  <div class="brand on-dark"><span class="mark"></span>VORK</div>
</section>

<section class="sheet envelope" aria-label="Envelope">
  <svg class="bg" viewBox="0 0 552 324" preserveAspectRatio="none" aria-hidden="true">
    <path d="M0 0H552V160C470 90 340 60 200 62C110 64 40 80 0 100Z" fill="var(--blue)"/>
    <path d="M0 10H552" stroke="var(--blue-dark)" stroke-width="2"/>
    <path d="M0 100C40 80 110 64 200 62C340 60 470 90 552 160" fill="none" stroke="var(--line)" stroke-width="2"/>
  </svg>
  <div class="flap-mark"></div>
  <div class="faint-name" aria-hidden="true">VORK</div>
  <div class="brand"><span class="mark"></span>VORK</div>
  <div class="sender">Calle Tepozan 58, Col. Las Brisas,<br>Distrito Federal, Mexico - 04260</div>
</section>

</body>
</html>
```